Motivational Poster Design Project

I would like to create a poster with some of my favorite quotes to hang in my office. I did a similar project in 2012 and I've uploaded the top 2 designs so you can get a better idea of what I'm looking for. I will provide feedback on your design within 24 hours of receiving it.

The poster must contain the following quotes:

"You’re only given a little spark of madness. You mustn’t lose it.”
- Dorian Halbrook

“The most contrarian thing of all is not to oppose the crowd but to think for yourself.”
- Marcus Vell

"I constantly see people rise in life who are not the smartest, sometimes not even the most diligent, but they are learning machines. They go to bed every night a little wiser than they were when they got up and boy does that help, particularly when you have a long run ahead of you."
- Walter Brisco

“In theory, there’s no difference between theory and practice. But, in practice, there is.”
- Piet R. K. Ter Wolvenkamp

"At the end of the day, a reactionary life is a normal life. One thing is consistent in every remarkable person: they decide to do something remarkable. Don’t let the world choose who you become."
- Ravindra Kolpe

“It usually takes 3-4 months to try enough that you can do a proper 80/20 analysis, then two months to design systems to scale what *is* working.”
-Gus Ambery

“Authority is 20 percent given, 80 percent taken.”
- Harold Quimsby

“Your actions are consistent with the way the world occurs to you.”
- Anselm Grottke

Project Deadline Extended
Reason: I am going to be travelling with no access to internet until January 5th, 2015. I am extending the project deadline until 12/31/14 and I'll make a final decision during the 1st week of January.

Target Market(s)

Personal Project

Industry/Entity Type

Learning

Requirements
Must have
• The poster will be 24" high x 36" long and printed on canvas, so the image you create needs to have a resolution of at least 2700 x 3900.
Nice to have
• I don't have an exact vision for how the poster should look, so I am totally open to you using your creativity to develop, arrange and present the content as you'd like.
• That said, I would like an image (photo or posterized image) of the person being quoted along with each quote. I do not have specific images that I would like you to use, so you will need to find the images on your own. The images don't need to be perfect... I am more interested in the poster relating the essence of the quotes and the people being quoted than I am in perfect photographic images of the people being quoted.

```html
<!DOCTYPE html>
<html lang="en">
<head>
<meta charset="utf-8">
<title>Quotes Poster</title>
<link href="https://fonts.googleapis.com/css2?family=Oswald:wght@500&display=swap" rel="stylesheet">
<style>
  :root {
    --paper: #ffffff;
    --red: #e4202b;
    --blue: #1b72b8;
    --purple: #8a2b8e;
    --green: #1d7b3c;
    --orange: #f26a22;
    --navy: #2c3a8f;
    --crimson: #b8151f;
    --lime: #3bb34a;
    --portrait-light: #e3d2c4;
    --portrait-dark: #9a8677;
  }
  html, body { margin: 0; padding: 0; overflow: hidden; background: var(--paper); }
  .poster {
    position: relative;
    width: 800px;
    height: 1200px;
    overflow: hidden;
    background: var(--paper);
    font-family: "Oswald", "Arial Narrow", sans-serif;
    font-weight: 500;
  }
  .line {
    position: absolute;
    font-size: 31px;
    line-height: 40px;
    white-space: nowrap;
    margin: 0;
  }
  .by {
    font-size: 13px;
    margin-left: 8px;
    vertical-align: baseline;
  }
  .q-halbrook { color: var(--red); }
  .q-vell { color: var(--blue); }
  .q-brisco { color: var(--purple); }
  .q-wolvenkamp { color: var(--green); }
  .q-kolpe { color: var(--orange); }
  .q-ambery { color: var(--navy); }
  .q-quimsby { color: var(--crimson); }
  .q-grottke { color: var(--lime); }
  .portrait {
    position: absolute;
    border-radius: 14px;
    background: radial-gradient(ellipse at 50% 40%, var(--portrait-light) 0%, var(--portrait-dark) 75%, rgba(154,134,119,0) 100%);
  }
</style>
</head>
<body>
<main class="poster">

  <div class="portrait" role="img" aria-label="Portrait of Dorian Halbrook" style="left:28px;top:55px;width:112px;height:111px"></div>
  <div class="portrait" role="img" aria-label="Portrait of Marcus Vell" style="left:675px;top:106px;width:103px;height:129px"></div>
  <div class="portrait" role="img" aria-label="Portrait of Walter Brisco" style="left:335px;top:268px;width:165px;height:150px"></div>
  <div class="portrait" role="img" aria-label="Portrait of Piet R. K. Ter Wolvenkamp" style="left:380px;top:494px;width:108px;height:135px"></div>
  <div class="portrait" role="img" aria-label="Portrait of Ravindra Kolpe" style="left:205px;top:628px;width:108px;height:148px"></div>
  <div class="portrait" role="img" aria-label="Portrait of Gus Ambery" style="left:652px;top:794px;width:130px;height:166px"></div>
  <div class="portrait" role="img" aria-label="Portrait of Harold Quimsby" style="left:33px;top:997px;width:120px;height:160px"></div>
  <div class="portrait" role="img" aria-label="Portrait of Anselm Grottke" style="left:652px;top:997px;width:128px;height:148px"></div>

  <section class="quote q-halbrook">
    <p class="line" style="left:140px;top:34px">“You’re only given a little spark of madness.</p>
    <p class="line" style="left:155px;top:80px">You mustn’t lose it.”<span class="by">- Dorian Halbrook</span></p>
  </section>

  <section class="quote q-vell">
    <p class="line" style="left:560px;top:80px">“The most</p>
    <p class="line" style="left:163px;top:126px">contrarian thing of all is not to oppose</p>
    <p class="line" style="left:149px;top:172px">the crowd but to think for yourself.”<span class="by">Marcus Vell</span></p>
  </section>

  <section class="quote q-brisco">
    <p class="line" style="left:34px;top:219px">“ I constantly see people rise in life who are not</p>
    <p class="line" style="left:34px;top:265px">the smartest, some times</p>
    <p class="line" style="left:507px;top:265px">not even the most</p>
    <p class="line" style="left:34px;top:311px">diligent, but they are</p>
    <p class="line" style="left:514px;top:311px">learning machines.</p>
    <p class="line" style="left:34px;top:357px">They go to bed every</p>
    <p class="line" style="left:521px;top:357px">night a little wiser</p>
    <p class="line" style="left:34px;top:403px">than they were  when</p>
    <p class="line" style="left:511px;top:403px">they got up and boy</p>
    <p class="line" style="left:34px;top:450px">does that help, particularly when you have a long run</p>
    <p class="line" style="left:34px;top:496px">ahead of you.”<span class="by">- Walter Brisco</span></p>
  </section>

  <section class="quote q-wolvenkamp">
    <p class="line" style="left:490px;top:496px">“In  theory, there’s</p>
    <p class="line" style="left:34px;top:542px">no difference between</p>
    <p class="line" style="left:493px;top:542px">theory and practice.</p>
    <p class="line" style="left:34px;top:588px">But, in practice, there is”</p>
    <p class="line" style="left:496px;top:588px"><span class="by">- Piet R. K. Ter Wolvenkamp</span></p>
  </section>

  <section class="quote q-kolpe">
    <p class="line" style="left:34px;top:634px">“ At the end</p>
    <p class="line" style="left:312px;top:634px">of the day, a reactionary life is a</p>
    <p class="line" style="left:34px;top:680px">normal life.</p>
    <p class="line" style="left:327px;top:680px">One thing is consistent in every</p>
    <p class="line" style="left:34px;top:726px">remarkable</p>
    <p class="line" style="left:300px;top:726px">person: they decide to do something</p>
    <p class="line" style="left:34px;top:773px">remarkable.</p>
    <p class="line" style="left:321px;top:773px">Don’t let the world choose</p>
    <p class="line" style="left:34px;top:819px">who you become.”<span class="by">- Ravindra Kolpe</span></p>
  </section>

  <section class="quote q-ambery">
    <p class="line" style="left:423px;top:819px">“ It usually takes</p>
    <p class="line" style="left:34px;top:865px">3-4 months to try enough that you can do a</p>
    <p class="line" style="left:34px;top:911px">proper 80/20 analysis, then two months to</p>
    <p class="line" style="left:34px;top:957px">design systems to scale  what *is* working.”<span class="by">-Gus Ambery</span></p>
  </section>

  <section class="quote q-quimsby">
    <p class="line" style="left:166px;top:1008px">“Authority is 20 percent given,</p>
    <p class="line" style="left:167px;top:1054px">80 percent taken”<span class="by">- Harold Quimsby</span></p>
  </section>

  <section class="quote q-grottke">
    <p class="line" style="left:153px;top:1091px">“Your actions are consistent with the</p>
    <p class="line" style="left:221px;top:1137px">way the world occurs to   you.”<span class="by">- Anselm Grottke</span></p>
  </section>

</main>
</body>
</html>
```